Kestrel Unity Front March 2013

I am seeking to create a flyer promoting the event May Day in Sydney. The Event is a March and will be taking place on the 5th May Sunday. The Projection of the flyer should be fresh and modern but capable of encapsulating values of struggle, justice and solidarity. It is an event that started in the late 1800's in a struggle to obtain the 8 hour day.
This flyer should capture the old logo with a fresh modern interpretation.

HI All, 

Can we add the following details to design. Apologies it came late, it just got forwarded onto me. 

Twitter (logo) @KestrelUnityFront
Facebook (logo) Unity Front Kestrel 2013

Thanks

Reason: I want to allow designers the opportunity to make revisions on their existing designs.

Reason: Last minute changes are not coming through.

General Public, Union Members, Workers, advocates of social justice and democracy

Event

• Event Details:
Kestrel Unity Front March
Sunday May 5th
Assembling: 11:30am
Marching: 12:00pm
Assembly Point: Tallowood Street outside Greyston Hall, Sydney
Kestrel Unity Front Logo (See Attachment) This logo should be manipulated to show a fresh and modern aspect to it, whilst retaing the same characteristics.

• Themes of the flyer should capture the following ideas:
International Workers Solidarity
Workers Rights
Fight for the 8 hour day
location being Sydney Australia
Images of
People Rallying, protesting, marching

```html
<!DOCTYPE html>
<html lang="en">
<head>
<meta charset="utf-8">
<title>Kestrel Unity Front March</title>
<link rel="stylesheet" href="https://fonts.googleapis.com/css2?family=Anton&display=swap">
<style>
  :root {
    --ink: #111111;
    --flame: #ff3b0a;
    --paper: #ffffff;
    --paper-tint: #f1f1f1;
    --night: #262626;
    --night-soft: #4a4a4a;
  }
  html, body {
    margin: 0;
    padding: 0;
    overflow: hidden;
    background: var(--paper);
  }
  .flyer {
    position: relative;
    width: 927px;
    height: 1200px;
    overflow: hidden;
    background: var(--paper);
  }
  .flyer__art {
    position: absolute;
    inset: 0;
    width: 927px;
    height: 1200px;
    display: block;
  }
  .title-line {
    font-family: "Anton", "Arial Narrow", sans-serif;
    fill: var(--flame);
    filter: drop-shadow(3px 4px 3px rgba(0,0,0,0.35));
  }
  .seal-name {
    font-family: "Anton", "Arial Narrow", sans-serif;
    fill: var(--paper);
    font-size: 17px;
    letter-spacing: 1px;
  }
  .event-line {
    font-family: "Anton", "Arial Narrow", sans-serif;
    fill: var(--ink);
  }
</style>
</head>
<body>
<main class="flyer">
  <svg class="flyer__art" viewBox="0 0 927 1200" xmlns="http://www.w3.org/2000/svg">
    <defs>
      <linearGradient id="nightTone" x1="0" y1="0" x2="1" y2="1">
        <stop offset="0" stop-color="var(--night-soft)"/>
        <stop offset="1" stop-color="var(--night)"/>
      </linearGradient>
      <linearGradient id="paperTone" x1="0" y1="0" x2="0" y2="1">
        <stop offset="0" stop-color="var(--paper-tint)"/>
        <stop offset="1" stop-color="var(--paper)"/>
      </linearGradient>
    </defs>

    <rect class="backdrop-light" x="0" y="0" width="927" height="1200" fill="url(#paperTone)"
          role="img" aria-label="Faint repeating pattern of raised fists"/>
    <polygon class="backdrop-dark" points="0,0 927,0 927,523 0,356" fill="url(#nightTone)"
             role="img" aria-label="Repeating pattern of white raised fists on dark ground"/>

    <g class="title">
      <text class="title-line" x="121" y="538" font-size="186" textLength="705" lengthAdjust="spacingAndGlyphs">KESTREL</text>
      <text class="title-line" x="121" y="724" font-size="186" textLength="272" lengthAdjust="spacingAndGlyphs">UNITY</text>
      <text class="title-line" x="540" y="724" font-size="186" textLength="286" lengthAdjust="spacingAndGlyphs">FRONT</text>
      <text class="title-line" x="94" y="939" font-size="240" textLength="742" lengthAdjust="spacingAndGlyphs">MARCH</text>
    </g>

    <g class="seal">
      <circle cx="466" cy="678" r="64" fill="var(--flame)" stroke="var(--paper)" stroke-width="5"/>
      <text class="seal-name" x="466" y="660" text-anchor="middle">KESTREL</text>
      <text class="seal-name" x="466" y="684" text-anchor="middle">UNITY</text>
      <text class="seal-name" x="466" y="708" text-anchor="middle">FRONT</text>
    </g>

    <g class="event-details">
      <text class="event-line" x="94" y="1118" font-size="54" textLength="739" lengthAdjust="spacingAndGlyphs">SUNDAY ★ MAY 5TH ★ 12:00PM</text>
      <text class="event-line" x="53" y="1163" font-size="40" textLength="823" lengthAdjust="spacingAndGlyphs">TALLOWOOD ST ★ OUTSIDE GREYSTON HALL SYDNEY</text>
    </g>
  </svg>
</main>
</body>
</html>
```